Lena Hartwell Web

Lena Hartwell is a singer/songwriter that has a presence in the market for over 20 years. She currently has a website, lenahartwell.example that needs a major makeover. IT needs to be reorganized to; 1) make it more user friendly; 2) enable multi-languages including; Spanish, French, Russian, Japanese, Chinese and Portuguese; 3) enable purchases online through a storefront of promotional merchandise and music tracks. She has a logo that needs an update, as well as we currently have a business card open on PixelBazaar for input. Working to re-brand, or refresh her brand.

Lena Hartwell is the next Rosa Delmont! She has 5 platinum records, Lumen Award nominations and tours with Harold Prescott globally and is Nora Vandermeer's key backup singer for 12 years.
Updates

Some common questions have come up.  Here is some further input:

1) Colors - No specific color in mind but probably earth tones.  Although at this point we''re completely open.  Lena likes classical style, Russian, French decor.  Paris architecture. Greek, Italian textures, Goddess like symbols from the Roman Empire, or the symbols and pomp of the British monarchy.  One name on tap for the new CD is "Lanterns Over Quiet Water"
2) Example website - I have not found a new one specifically, but what I don''t like about the existing one is it is not easy to navigate.  Needs to be streamlined and easy to navigate with a storefront for merchandise and music downloads.  
3) On Logo - We''re revamping a "Global" merchandise rollout logo.  We''ve also considered possibly modifying the old english "Hartwell" family crest which signifies royalty, but have not explored that too much.  The hexagon yellow logo on her current website, I was thinking of modifying to gold (brushed - or polished?), then taking the LH lettering using a fountain pen type look there the line thickness flows with pressure on the pen, then make the gold look like a pillow, with the letter making an impression into the gold pillow.  This expands to a high quality pin, blinged up broach with diamonds imbedded for example, Global label identity, tee shirts, label tag on fashion clothing etc etc. 
 4) One thing marketing has asked us to build is a routine video blog to reach out to fans in a personal way.  Short clips of daily activity, travel prep for shows, etc. Possibly a signup/fanpage where people get emails sent back whenever anything new is posted, like a video blog, new pics, new events.  A menu to choose what you get updates on. 

Thanks, Dennis

Target Market(s)

1) Fan base in Europe, Asia, Latin America and North America
2) Movie producers seeking soundtracks
3) Private clients seeking an outstanding performer for corporate events

Industry/Entity Type

Singer

Requirements
Must have
• Better organization into smaller pages. Items critical include: 1) music tracks, 2) ClipStream links, 3) photos & Video, 4) storefront to enable online merchandise purchase 5) a way to illustrate her genre from; gospel, to rock, funk, R&B, country,

```html
<!DOCTYPE html>
<html lang="en">
<head>
<meta charset="utf-8">
<title>Lena Hartwell</title>
<link href="https://fonts.googleapis.com/css2?family=Open+Sans:wght@300;400;600;700&display=swap" rel="stylesheet">
<style>
:root{
  --gold:#b8892a;
  --gold-dark:#8f6a1e;
  --gold-band:#c39a35;
  --charcoal:#3b3b3d;
  --charcoal-dark:#2c2c2e;
  --ink:#333;
  --muted:#666;
  --paper:#ffffff;
  --mist:#eeeeef;
  --red:#c0392b;
  --white:#fff;
}
*{box-sizing:border-box;margin:0;padding:0}
html,body{width:1200px;height:2244px;overflow:hidden}
body{font-family:"Open Sans",Arial,sans-serif;color:var(--ink);background:var(--paper);position:relative}

/* hero */
.hero{position:absolute;left:0;top:0;width:1200px;height:600px;overflow:hidden}
.hero-photo{position:absolute;inset:0;background:
  radial-gradient(ellipse 260px 420px at 640px 330px,#c8a45e 0%,#8a6628 40%,transparent 75%),
  linear-gradient(90deg,#1e160b 0%,#4a3516 35%,#6e5022 55%,#3a2a12 80%,#1b140a 100%)}
.nav-bar{position:absolute;left:0;top:0;width:1200px;height:50px;background:rgba(0,0,0,.55)}
.logo{position:absolute;left:150px;top:0;width:64px;height:78px}
.logo-mark{position:absolute;left:0;top:0;width:64px;height:78px;background:var(--gold);display:flex;align-items:center;justify-content:center;color:var(--white);font-weight:600;font-size:20px}
.nav{position:absolute;right:138px;top:16px;display:flex;gap:22px;list-style:none}
.nav li{color:var(--white);font-size:13px;font-weight:600;letter-spacing:.5px}
.hero-title{position:absolute;left:290px;top:248px;color:var(--white);font-weight:300;font-size:64px;line-height:70px;letter-spacing:1px}
.hero-arrow{position:absolute;top:296px;width:44px;height:56px;background:rgba(0,0,0,.75);display:flex;align-items:center;justify-content:center}
.hero-dots{position:absolute;left:220px;top:552px;display:flex;gap:8px}
.hero-dots span{width:12px;height:12px;border-radius:50%;background:rgba(255,255,255,.55)}
.hero-dots span.on{background:var(--white)}

/* welcome */
.welcome{position:absolute;left:0;top:600px;width:1200px;height:240px;background:var(--paper);text-align:center}
.section-title{font-weight:400;font-size:34px}
.welcome .section-title{position:absolute;left:0;right:0;top:22px;color:var(--gold-dark)}
.welcome p{position:absolute;left:150px;width:900px;top:80px;font-size:13px;line-height:21px;color:var(--muted)}
.btn{display:inline-block;background:var(--gold);color:var(--white);font-size:14px;font-weight:600;padding:8px 22px}
.welcome .btn{position:absolute;left:537px;top:176px}

/* photo gallery */
.photos{position:absolute;left:0;top:840px;width:1200px;height:400px;background:var(--charcoal)}
.photos .section-title{position:absolute;left:0;right:0;top:24px;text-align:center;color:var(--white)}
.photo{position:absolute;top:96px;width:214px;height:222px}
.round-arrow{position:absolute;top:186px;width:44px;height:44px;border-radius:50%;background:#666;display:flex;align-items:center;justify-content:center}
.photos .btn{position:absolute;left:552px;top:360px;padding:10px 24px}

/* video gallery */
.videos{position:absolute;left:0;top:1240px;width:1200px;height:604px;background:var(--gold-band)}
.videos .section-title{position:absolute;left:0;right:0;top:20px;text-align:center;color:var(--white)}
.video-main{position:absolute;left:156px;top:92px;width:604px;height:364px;background:linear-gradient(120deg,#2a1a10,#6a4a30 45%,#b59b7a 70%,#3a2a20)}
.player-bar{position:absolute;left:156px;top:456px;width:604px;height:26px;background:#e8e8e8;border-top:4px solid var(--red)}
.play{position:absolute;left:418px;top:236px;width:44px;height:36px;border-radius:8px;background:var(--red)}
.thumb{position:absolute;left:780px;width:230px;height:116px}
.clip-brand{position:absolute;left:156px;top:504px;display:flex;align-items:center;gap:14px}
.clip-name{font-size:28px;font-weight:700;color:var(--charcoal-dark)}
.btn-red{background:var(--red);color:var(--white);font-size:13px;font-weight:600;padding:7px 16px}
.clip-cta{font-size:15px;color:var(--white)}

/* music player strip */
.music{position:absolute;left:0;top:1844px;width:1200px;height:120px;background:var(--paper)}
.album{position:absolute;left:176px;top:10px;width:104px;height:104px;background:linear-gradient(135deg,#222,#555)}
.track-bar{position:absolute;left:296px;top:26px;width:756px;height:74px;background:linear-gradient(#4a4a4a,#1e1e1e);border-radius:6px}
.track-play{position:absolute;left:14px;top:12px;width:32px;height:32px;border-radius:50%;background:var(--gold)}
.track-meta{position:absolute;left:56px;top:8px;color:#ddd;font-size:11px;line-height:15px}
.track-meta b{color:var(--white);font-size:13px;font-weight:600}
.wave{position:absolute;left:14px;top:52px;width:728px;height:14px;background:repeating-linear-gradient(90deg,#888 0 2px,transparent 2px 4px)}

/* newsletter + footer */
.subscribe{position:absolute;left:0;top:1964px;width:1200px;height:280px;background:var(--mist)}
.subscribe h2{position:absolute;left:0;right:0;top:42px;text-align:center;font-size:17px;font-weight:700;color:var(--red);letter-spacing:.5px}
.sub-input{position:absolute;left:520px;top:114px;width:160px;height:32px;background:var(--white);border:1px solid #ccc;font-size:11px;color:#888;padding:8px 10px}
.subscribe .btn{position:absolute;left:692px;top:114px;height:32px;padding:6px 28px}
.connect{position:absolute;left:156px;top:192px;font-size:11px;color:var(--muted)}
.social{position:absolute;left:156px;top:214px;display:flex;gap:8px}
.social span{width:22px;height:22px;border-radius:50%}
.footer-links{position:absolute;right:156px;top:204px;font-size:10px;color:var(--muted);letter-spacing:.3px}
.copyright{position:absolute;right:156px;top:224px;font-size:10px;color:#888}
</style>
</head>
<body>

<header class="hero">
  <div class="hero-photo" role="img" aria-label="Sepia stage photo of the singer performing at a microphone"></div>
  <div class="nav-bar"></div>
  <div class="logo"><div class="logo-mark">LH</div></div>
  <ul class="nav">
    <li>HOME</li><li>EVENTS</li><li>MUSIC</li><li>VIDEO</li><li>PICTURES</li><li>ABOUT</li><li>DISCOGRAPHY</li><li>CONTACT</li>
  </ul>
  <h1 class="hero-title">LENA<br>HARTWELL</h1>
  <div class="hero-arrow" style="left:128px"><svg width="14" height="20"><path d="M11 2 3 10l8 8" stroke="#fff" stroke-width="3" fill="none"/></svg></div>
  <div class="hero-arrow" style="left:1028px"><svg width="14" height="20"><path d="M3 2l8 8-8 8" stroke="#fff" stroke-width="3" fill="none"/></svg></div>
  <div class="hero-dots"><span></span><span></span><span class="on"></span><span></span><span></span></div>
</header>

<section class="welcome">
  <h2 class="section-title">Welcome to Our Site</h2>
  <p>With a powerfully unique voice and a definitive sound, Lena Hartwell consistently delivers soul stirring performances that captivate audiences around the world. Using her past as a spring board, Lena channels memories into melodies that are proud and strong. Her rich melodic sound and exciting performance style are rooted in the story of a pastor's daughter with a passion for singing gospel music.</p>
  <span class="btn">Read More &rarr;</span>
</section>

<section class="photos">
  <h2 class="section-title">Photo Gallery</h2>
  <div class="round-arrow" style="left:72px"><svg width="12" height="16"><path d="M9 2 3 8l6 6" stroke="#ddd" stroke-width="2.5" fill="none"/></svg></div>
  <div class="photo" role="img" aria-label="Singer on stage in warm red light" style="left:148px;background:linear-gradient(150deg,#7a1e10,#c0622a 50%,#3a1008)"></div>
  <div class="photo" role="img" aria-label="Black and white photo of the singer" style="left:378px;background:linear-gradient(150deg,#222,#9a9a9a 55%,#333)"></div>
  <div class="photo" role="img" aria-label="Live concert shot in blue and teal light" style="left:608px;background:linear-gradient(150deg,#0d1a2a,#2a7a8a 50%,#0a0f18)"></div>
  <div class="photo" role="img" aria-label="Singer in blue stage lighting" style="left:838px;background:linear-gradient(150deg,#0a2a8a,#3a6ad8 50%,#1a0a30)"></div>
  <div class="round-arrow" style="left:1084px"><svg width="12" height="16"><path d="M3 2l6 6-6 6" stroke="#ddd" stroke-width="2.5" fill="none"/></svg></div>
  <span class="btn">View More</span>
</section>

<section class="videos">
  <h2 class="section-title">Video Gallery</h2>
  <div class="video-main" role="img" aria-label="Featured music video still of the singer"></div>
  <div class="play"><svg width="44" height="36"><path d="M18 11l10 7-10 7z" fill="#fff"/></svg></div>
  <div class="player-bar"></div>
  <div class="thumb" role="img" aria-label="Video thumbnail, stage performance" style="top:92px;background:linear-gradient(135deg,#5a1a10,#c8642a)"></div>
  <div class="thumb" role="img" aria-label="Video thumbnail, interview" style="top:222px;background:linear-gradient(135deg,#f0e6e0,#c05050)"></div>
  <div class="thumb" role="img" aria-label="Video thumbnail, concert crowd" style="top:352px;background:linear-gradient(135deg,#e8e0e0,#b03a3a)"></div>
  <div class="clip-brand">
    <span class="clip-name">ClipStream</span>
    <span class="btn-red">Click Here</span>
    <span class="clip-cta">to Watch our Videos</span>
  </div>
</section>

<section class="music">
  <div class="album" role="img" aria-label="Album cover artwork"></div>
  <div class="track-bar">
    <div class="track-play"></div>
    <div class="track-meta">Lena Hartwell<br><b>Where The Quiet Rivers Go</b></div>
    <div class="wave"></div>
  </div>
</section>

<footer class="subscribe">
  <h2>SUBSCRIBE TO OUR NEWSLETTER</h2>
  <div class="sub-input">Enter your Email Id</div>
  <span class="btn">Sign Up</span>
  <div class="connect">Connect with us</div>
  <div class="social"><span style="background:#3b5998"></span><span style="background:#33aaee"></span><span style="background:#e8732a"></span></div>
  <div class="footer-links">HOME | EVENTS | MUSIC | VIDEO | PICTURES | ABOUT | DISCOGRAPHY | CONTACT</div>
  <div class="copyright">Copyright 2014 &copy; All Rights Reserved</div>
</footer>

</body>
</html>
```